Dog Food Bag Packaging Redesign

Hey there..We're a small dog food company, focusing on all natural, locally sourced, high quality ingredients. They're patties, and baked for 10 min. Dogs go insane for them. We're looking to redo our packaging, and thus, its design. I've attached images. Currently, we are wrapping 12 patties in a poly bag and then butcher paper, and sticking a label on it. We're moving to a zipper seal poly that's black. I've attached the design concept from our bag manufacturer for your reference only. We don't necessarily want to use our old label, but we're not against using elements of it. We really like our current label.. I'm just not so sure it's the right call for a poly bag.We have three flavours; chicken, beef, lamb. I would LOVE to know what flavour the bag is without having to be super close to the bag. So perhaps the top part (1-4 inches) could be the flavour colour? I will have to provide some verbiage for the back. I need to add feeding instructions, and a bit of a thank you story. I'm open for suggestions on how to display ingredients/nutritional facts.

Target Market(s)

Dog Owners

Industry/Entity Type

Manufacturing

Font styles to use
Sans Serif

Colors
9bcb3c

Requirements
Must have
• Total bag design. When you submit your design, please submit your designs on top of a bag. It makes it much easier to visual the end product.
• The bag needs to have the associated flavour colours on it to differentiate flavour from a distance. Red = beef, yellow = chicken, purple = lamb.
• I'm happy with the logo being on the back only, but if on the front it needs to be small. Patties should be the main header word.
Nice to have
• I like the idea of a vertical colour bar on the side of the bag to show its flavour, but I'm not again a top horizontal bar either.
• I like PATTIES being the biggest word on the bag.

```html
<!DOCTYPE html>
<html lang="en">
<head>
<meta charset="utf-8">
<title>Pawfield Deboned Chicken Patties – Bag Front and Back</title>
<link href="https://fonts.googleapis.com/css2?family=Anton&family=Oswald:wght@300;400;500;600&family=Bebas+Neue&display=swap" rel="stylesheet">
<style>
  :root {
    --bg: #e6e7e8;
    --bag: #fbfbfb;
    --yellow: #f2cd2e;
    --yellow-soft: #f6d84a;
    --orange: #e0922a;
    --orange-deep: #d98424;
    --green: #4f9a2f;
    --green-light: #9bcb3c;
    --green-text: #3f9a37;
    --brown: #5a3a1e;
    --ink: #222222;
    --grey-photo-a: #c9c9c9;
    --grey-photo-b: #6f6f6f;
  }
  * { box-sizing: border-box; margin: 0; padding: 0; }
  html, body { width: 1200px; height: 891px; overflow: hidden; }
  body { background: var(--bg); position: relative; font-family: "Oswald", sans-serif; color: var(--ink); }

  .bag {
    position: absolute; top: 89px; width: 457px; height: 702px;
    background: var(--bag); overflow: hidden;
    box-shadow: 0 2px 10px rgba(0,0,0,.12);
  }
  .bag--front { left: 113px; }
  .bag--back { left: 612px; }

  .size-ribbon { position: absolute; left: 330px; top: 0; width: 62px; height: 96px; }
  .size-ribbon__weight {
    height: 38px; background: var(--orange); color: var(--yellow-soft);
    font-family: "Bebas Neue", sans-serif; font-size: 26px; text-align: center; line-height: 40px;
  }
  .size-ribbon__count {
    height: 58px; background: var(--yellow); color: #fbe9a0;
    font-family: "Bebas Neue", sans-serif; font-size: 12px; text-align: center; padding-top: 12px;
    clip-path: polygon(0 0,100% 0,100% 100%,50% 82%,0 100%);
  }

  .brand { position: absolute; text-align: center; }
  .brand__dot { width: 44px; height: 44px; border-radius: 50%; background: var(--green); margin: 0 auto 6px; }
  .brand__name { font-family: "Oswald", sans-serif; font-weight: 500; font-size: 22px; letter-spacing: 1px; color: var(--brown); }
  .bag--front .brand { left: 305px; top: 104px; width: 120px; }
  .bag--back .brand { left: 310px; top: 94px; width: 110px; }
  .bag--back .brand__dot { width: 36px; height: 36px; }
  .bag--back .brand__name { font-size: 19px; }

  .front-kicker {
    position: absolute; left: 20px; top: 420px; transform-origin: 0 0; transform: rotate(-90deg);
    font-family: "Bebas Neue", sans-serif; color: var(--orange); font-size: 20px; letter-spacing: 15.5px; white-space: nowrap;
  }
  .front-title {
    position: absolute; left: 58px; top: 420px; transform-origin: 0 0; transform: rotate(-90deg) scaleY(1.05);
    font-family: "Anton", sans-serif; color: var(--yellow); font-size: 124px; line-height: 118px; letter-spacing: -1px; white-space: nowrap;
  }

  .photo { position: absolute; }
  .photo--dog-front { left: 265px; top: 200px; width: 192px; height: 444px; background: linear-gradient(160deg, var(--grey-photo-a), var(--grey-photo-b)); border-radius: 40% 0 0 0; }
  .photo--patties { left: 184px; top: 534px; width: 110px; height: 106px; background: radial-gradient(circle at 55% 60%, #b48a4f, #8c6637 70%, transparent 72%); }
  .photo--dog-back { left: 384px; top: 460px; width: 68px; height: 186px; background: linear-gradient(160deg, var(--grey-photo-a), var(--grey-photo-b)); border-radius: 45% 0 0 0; z-index: 0; }

  .flavour-band {
    position: absolute; left: 15px; top: 442px; width: 330px; height: 72px; background: var(--orange);
    display: flex; align-items: center; padding-left: 22px; z-index: 1;
  }
  .flavour-band__name { font-family: "Bebas Neue", sans-serif; font-size: 70px; color: var(--yellow-soft); letter-spacing: 6px; line-height: 1; padding-top: 6px; }
  .flavour-band__stars { color: var(--yellow-soft); font-size: 9px; margin-left: 14px; letter-spacing: 1px; }

  .key-ingredients { position: absolute; left: 40px; top: 536px; width: 126px; list-style: none; }
  .key-ingredients li {
    font-family: "Bebas Neue", sans-serif; font-size: 11.5px; letter-spacing: 1.6px; color: var(--brown);
    border-bottom: 1px solid var(--orange); padding: 3px 0 2px 22px; position: relative; white-space: nowrap;
  }
  .key-ingredients li::before { content: ""; position: absolute; left: 5px; top: 6px; width: 7px; height: 7px; border-radius: 50%; background: #a23a1a; }

  .footer { position: absolute; left: 0; bottom: 0; width: 100%; height: 58px; z-index: 2; }
  .footer svg { position: absolute; inset: 0; }
  .footer__row { position: absolute; left: 22px; right: 12px; top: 14px; display: flex; align-items: center; color: #e8f2d6; font-family: "Bebas Neue", sans-serif; }
  .footer__site { font-size: 20px; letter-spacing: 3px; }
  .footer__sep { width: 9px; height: 9px; border-radius: 50%; background: #2d6a1c; margin: 0 22px; }
  .footer__origin { display: flex; align-items: center; gap: 10px; font-size: 10px; letter-spacing: 2px; line-height: 1.2; }
  .footer__badges { display: flex; gap: 12px; }
  .badge { text-align: center; font-size: 7px; letter-spacing: 1px; }
  .badge__shape { width: 18px; height: 18px; border-radius: 50%; border: 1.5px solid #e8f2d6; margin: 0 auto 2px; }

  .back-kicker { position: absolute; left: 33px; top: 104px; font-family: "Bebas Neue", sans-serif; font-size: 20px; letter-spacing: 10px; color: var(--orange); white-space: nowrap; }
  .back-title { position: absolute; left: 32px; top: 122px; font-family: "Anton", sans-serif; font-size: 96px; line-height: 1; color: var(--yellow); transform-origin: 0 0; transform: scaleX(.72); white-space: nowrap; }

  .nutrition { position: absolute; left: 36px; top: 226px; width: 175px; border: 3px solid var(--ink); background: #fff; padding: 6px 5px 4px; }
  .nutrition__title { font-family: "Oswald", sans-serif; font-weight: 600; font-size: 26px; line-height: 1; letter-spacing: -.5px; }
  .nutrition__basis { font-family: "Oswald", sans-serif; font-weight: 500; font-size: 11px; border-bottom: 4px solid var(--ink); padding: 3px 0 4px; }
  .nutrition__row { display: flex; justify-content: space-between; font-family: "Oswald", sans-serif; font-size: 12px; padding: 3px 0 2px; border-bottom: 1px solid var(--green); }
  .nutrition__row:last-child { border-bottom: none; }

  .ingredients { position: absolute; left: 44px; top: 450px; width: 165px; }
  .ingredients__title { font-family: "Oswald", sans-serif; font-weight: 600; font-size: 15px; border-bottom: 2px solid var(--green); display: inline-block; margin-bottom: 8px; }
  .ingredients__text { font-family: "Oswald", sans-serif; font-weight: 300; font-size: 10px; line-height: 1.6; text-align: justify; text-transform: uppercase; }

  .info-box { position: absolute; left: 238px; width: 190px; border: 1.5px solid var(--green-light); border-radius: 10px 0 10px 10px; overflow: hidden; background: #fff; z-index: 1; }
  .info-box--health { top: 168px; height: 186px; }
  .info-box--feeding { top: 400px; height: 224px; width: 176px; }
  .info-box__head { background: linear-gradient(90deg, var(--green-light), var(--green)); color: #f2f7e6; font-family: "Bebas Neue", sans-serif; font-size: 19px; padding: 8px 9px 3px; border-radius: 0 10px 0 0; }
  .info-box__list { list-style: none; padding: 8px 8px 0 10px; }
  .info-box__list li { margin-bottom: 6px; }
  .info-box__term { font-family: "Oswald", sans-serif; font-weight: 500; font-size: 12px; display: inline-block; border-bottom: 1.5px solid var(--green-light); padding-left: 10px; position: relative; }
  .info-box__term::before { content: ""; position: absolute; left: 0; top: 5px; border-left: 6px solid var(--green); border-top: 4px solid transparent; border-bottom: 4px solid transparent; }
  .info-box__desc { font-family: "Oswald", sans-serif; font-weight: 300; font-size: 7.3px; line-height: 1.45; padding: 4px 0 0 10px; text-transform: uppercase; }

  .callout { position: absolute; left: 238px; display: flex; align-items: center; gap: 8px; font-family: "Bebas Neue", sans-serif; color: var(--green-text); letter-spacing: .3px; z-index: 1; }
  .callout--promise { top: 362px; width: 190px; justify-content: space-between; font-size: 11.5px; text-align: center; line-height: 1.35; }
  .callout--loyal { top: 631px; font-size: 12px; white-space: nowrap; }
  .arrow { width: 20px; height: 20px; flex: none; }
</style>
</head>
<body>

<section class="bag bag--front" aria-label="Bag front">
  <div class="size-ribbon">
    <div class="size-ribbon__weight">3 LB</div>
    <div class="size-ribbon__count">12 PATTIES</div>
  </div>

  <div class="brand">
    <div class="brand__dot"></div>
    <div class="brand__name">PAWFIELD</div>
  </div>

  <div class="front-kicker">DEBONED CHICKEN</div>
  <h1 class="front-title">PATTIES</h1>

  <div class="photo photo--dog-front" role="img" aria-label="Black and white photograph of a dog looking up"></div>

  <div class="flavour-band">
    <span class="flavour-band__name">CHICKEN</span>
    <span class="flavour-band__stars">★★★★★</span>
  </div>

  <ul class="key-ingredients">
    <li>DEBONED CHICKEN</li>
    <li>FRESH EGGS</li>
    <li>APPLE, SWEET POTATOS</li>
    <li>BROCOLI</li>
    <li>CARROTS</li>
  </ul>

  <div class="photo photo--patties" role="img" aria-label="Photograph of a stack of baked chicken patties"></div>

  <footer class="footer">
    <svg width="457" height="58" viewBox="0 0 457 58" preserveAspectRatio="none" aria-hidden="true">
      <path d="M0 8 Q228 -2 457 6 L457 58 L0 58 Z" fill="var(--green)"/>
    </svg>
    <div class="footer__row">
      <span class="footer__site">GOPAWFIELD.CA</span>
      <span class="footer__sep"></span>
      <span class="footer__origin">PROUDLY<br>CANADIAN</span>
      <span class="footer__sep"></span>
      <div class="footer__badges">
        <div class="badge"><div class="badge__shape"></div>FRESH</div>
        <div class="badge"><div class="badge__shape"></div>LOCAL</div>
        <div class="badge"><div class="badge__shape"></div>RESPONSIBLE</div>
      </div>
    </div>
  </footer>
</section>

<section class="bag bag--back" aria-label="Bag back">
  <div class="size-ribbon">
    <div class="size-ribbon__weight">3 LB</div>
    <div class="size-ribbon__count">12 PATTIES</div>
  </div>

  <div class="brand">
    <div class="brand__dot"></div>
    <div class="brand__name">PAWFIELD</div>
  </div>

  <div class="back-kicker">DEBONED CHICKEN</div>
  <h2 class="back-title">PATTIES</h2>

  <div class="nutrition">
    <div class="nutrition__title">Nutrition Facts</div>
    <div class="nutrition__basis">"PER 100G</div>
    <div class="nutrition__row"><span>PROTEIN</span><span>18.43%</span></div>
    <div class="nutrition__row"><span>FAT</span><span>9.84%</span></div>
    <div class="nutrition__row"><span>FIBRE</span><span>0.6%</span></div>
    <div class="nutrition__row"><span>CALORIES</span><span>224</span></div>
    <div class="nutrition__row"><span>MOISTURE</span><span>49.2%</span></div>
    <div class="nutrition__row"><span>DRY MATTER</span><span>49.7%</span></div>
  </div>

  <div class="ingredients">
    <div class="ingredients__title">INGREDIENTS</div>
    <p class="ingredients__text">Deboned chicken (muscle &amp; organ meat), fresh eggs, apples, sweet potatoes, broccoli, carrots, rolled oats, water, oat flour, brown rice flour, organic spelt flour, oregano, marjoram, alfalfa, carob powder, parsley, garlic powder, ginger, rosemary, torula yeast, lecithin, kelp, egg shells, vitamin C powder</p>
  </div>

  <div class="photo photo--dog-back" role="img" aria-label="Black and white photograph of a dog"></div>

  <div class="info-box info-box--health">
    <div class="info-box__head">HEALTHY EATING</div>
    <ul class="info-box__list">
      <li><span class="info-box__term">Homemade</span><p class="info-box__desc">Freshly prepared, gently cooked</p></li>
      <li><span class="info-box__term">Digestible</span><p class="info-box__desc">Nutrients stay in your dog, not her stool</p></li>
      <li><span class="info-box__term">Whole</span><p class="info-box__desc">Simple, familiar foods like eggs,<br>sweet potatoes &amp; meat</p></li>
    </ul>
  </div>

  <div class="callout callout--promise">
    <svg class="arrow" viewBox="0 0 20 20" aria-hidden="true"><path d="M0 2 L9 10 L0 18Z M9 2 L18 10 L9 18Z" fill="var(--green-text)"/></svg>
    <span>WE ONLY USE REAL INGREDIENTS -<br>NO FILLERS OR PRESERVATIVES</span>
    <svg class="arrow" viewBox="0 0 20 20" aria-hidden="true"><path d="M20 2 L11 10 L20 18Z M11 2 L2 10 L11 18Z" fill="var(--green-text)"/></svg>
  </div>

  <div class="info-box info-box--feeding">
    <div class="info-box__head">EASY FEEDING</div>
    <ul class="info-box__list">
      <li><span class="info-box__term">Simple</span><p class="info-box__desc">1 patty/day per 18lbs of dog</p></li>
      <li><span class="info-box__term">Easy</span><p class="info-box__desc">Thaw for an hour, or overnight<br>in fridge, or serve frozen</p></li>
      <li><span class="info-box__term">Clean</span><p class="info-box__desc">Break into bite-sized<br>pieces &amp; serve as meal <b>or,</b><br>use as high-value<br>training reward</p></li>
    </ul>
  </div>

  <div class="callout callout--loyal">
    <svg class="arrow" viewBox="0 0 20 20" aria-hidden="true"><path d="M0 2 L9 10 L0 18Z M9 2 L18 10 L9 18Z" fill="var(--green-text)"/></svg>
    <span>SHE WON'T LEAVE YOUR SIDE</span>
  </div>

  <footer class="footer">
    <svg width="457" height="58" viewBox="0 0 457 58" preserveAspectRatio="none" aria-hidden="true">
      <path d="M0 8 Q228 -2 457 6 L457 58 L0 58 Z" fill="var(--green)"/>
    </svg>
    <div class="footer__row">
      <span class="footer__site">GOPAWFIELD.CA</span>
      <span class="footer__sep"></span>
      <span class="footer__origin">PROUDLY<br>CANADIAN</span>
      <span class="footer__sep"></span>
      <div class="footer__badges">
        <div class="badge"><div class="badge__shape"></div>FRESH</div>
        <div class="badge"><div class="badge__shape"></div>LOCAL</div>
        <div class="badge"><div class="badge__shape"></div>RESPONSIBLE</div>
      </div>
    </div>
  </footer>
</section>

</body>
</html>
```